Alberta, Canada based Environmental Oilfield Consultant need a Business Card Design

We need a business card design for a year old company based in Edmonton, Alberta, Canada called Brambleton Consulting Inc. We are environmental consultants primarily for oilfield based companies (pipeline cleanup, site consultations, environmental site training, and site evaluations).

We like the color blue or green, something very clean and crisp looking.
We don't really care if there is an otter on it but most of our work is land based and nothing really to do with oceans or larger bodies of water.

The name Brambleton was the name of our fathers boat, and named our company that in his memory.

```html
<!DOCTYPE html>
<html lang="en">
<head>
<meta charset="utf-8">
<title>Brambleton Consulting Inc. – Business Card</title>
<link href="https://fonts.googleapis.com/css2?family=Questrial&display=swap" rel="stylesheet">
<style>
  :root {
    --page-bg: #2a2a2a;
    --card-top: #222325;
    --card-bottom: #050505;
    --brand-green: #9ccc2e;
    --name-green: #8cc63f;
    --contact-lime: #d4e63a;
    --icon-green: #7fbf3a;
  }
  * { margin: 0; padding: 0; box-sizing: border-box; }
  html, body {
    width: 1200px;
    height: 800px;
    overflow: hidden;
    background: var(--page-bg);
    font-family: "Questrial", "Century Gothic", sans-serif;
  }
  .canvas {
    position: relative;
    width: 1200px;
    height: 800px;
    display: flex;
    align-items: center;
    justify-content: center;
  }
  .business-card {
    position: relative;
    width: 840px;
    height: 480px;
    background: radial-gradient(ellipse at 55% 30%, var(--card-top) 0%, var(--card-bottom) 75%);
    box-shadow: 0 20px 50px rgba(0, 0, 0, 0.55);
  }
  .brand {
    position: absolute;
    left: 70px;
    top: 86px;
    display: flex;
    align-items: center;
    gap: 22px;
    color: var(--brand-green);
  }
  .brand-dot {
    width: 78px;
    height: 78px;
    border-radius: 50%;
    background: var(--brand-green);
  }
  .brand-name {
    display: flex;
    flex-direction: column;
    line-height: 1;
  }
  .brand-name .primary {
    font-size: 58px;
    letter-spacing: 2px;
  }
  .brand-name .secondary {
    font-size: 20px;
    letter-spacing: 12px;
    margin-top: 8px;
  }
  .contact-block {
    position: absolute;
    left: 110px;
    top: 262px;
  }
  .person-name {
    color: var(--name-green);
    font-size: 28px;
    font-weight: bold;
  }
  .person-role {
    color: var(--name-green);
    font-size: 18px;
    margin-top: 2px;
    margin-left: 10px;
  }
  .contact-list {
    list-style: none;
    margin-top: 38px;
    margin-left: 40px;
  }
  .contact-list li {
    display: flex;
    align-items: center;
    gap: 10px;
    color: var(--contact-lime);
    font-size: 26px;
    line-height: 1.25;
  }
  .contact-icon {
    width: 22px;
    height: 22px;
    flex: none;
  }
</style>
</head>
<body>
<main class="canvas">
  <section class="business-card">
    <div class="brand">
      <span class="brand-dot"></span>
      <div class="brand-name">
        <span class="primary">BRAMBLETON</span>
        <span class="secondary">CONSULTING INC.</span>
      </div>
    </div>

    <div class="contact-block">
      <p class="person-name">Dana Hollis</p>
      <p class="person-role">Director</p>
      <ul class="contact-list">
        <li>
          <svg class="contact-icon" viewBox="0 0 24 24" aria-hidden="true">
            <path fill="var(--icon-green)" d="M6.6 10.8a15.1 15.1 0 0 0 6.6 6.6l2.2-2.2a1 1 0 0 1 1-.25 11.4 11.4 0 0 0 3.6.57 1 1 0 0 1 1 1V20a1 1 0 0 1-1 1A17 17 0 0 1 3 4a1 1 0 0 1 1-1h3.5a1 1 0 0 1 1 1c0 1.25.2 2.45.57 3.57a1 1 0 0 1-.25 1z"/>
          </svg>
          0412 387 905
        </li>
        <li>
          <svg class="contact-icon" viewBox="0 0 24 24" aria-hidden="true">
            <rect x="2" y="5" width="20" height="14" rx="2" fill="var(--icon-green)"/>
            <path d="M3 6.5l9 6.5 9-6.5" fill="none" stroke="#0b0b0b" stroke-width="1.6"/>
          </svg>
          dana@brambletonconsulting.com
        </li>
        <li>
          <svg class="contact-icon" viewBox="0 0 24 24" aria-hidden="true">
            <circle cx="12" cy="12" r="10" fill="var(--icon-green)"/>
            <g fill="none" stroke="#0b0b0b" stroke-width="1.3">
              <ellipse cx="12" cy="12" rx="4.5" ry="10"/>
              <path d="M2 12h20M4 7h16M4 17h16M12 2v20"/>
            </g>
          </svg>
          www.brambletonconsulting.com
        </li>
      </ul>
    </div>
  </section>
</main>
</body>
</html>
```